Mara Penwick Concert Poster

I am a fulltime Christian singer from NZ. I need a new Concert Poster.
Specs: Color pic supplied but prefer b&w. Portrait orientation, not landscape. Copy supplied (to appear on bottom half of poster). Need blank box or strip near bottom for local venue details. Signature-style 'Mara Penwick' title across the photo or across the top, but totally open to design ideas/suggestion.

Target Market(s)

Mainly churches where I sing..

Industry/Entity Type

Singer

Requirements
Must have
• From past experience I have found a dark (even black) background, has most impact, with copy reversed out.. But as above, I am open to suggestions re color and feel. View my music on Vidorra for additional feel ideas.
Nice to have
• Simple direct classy style best, with minimal clutter.

```html
<!DOCTYPE html>
<html lang="en">
<head>
<meta charset="utf-8">
<title>Mara Penwick Concert Poster</title>
<link href="https://fonts.googleapis.com/css2?family=Anton&family=Oswald:wght@500;700&family=Lora:ital@1&display=swap" rel="stylesheet">
<style>
  :root {
    --ink: #0b0b0b;
    --paper: #ffffff;
    --accent: #f39a36;
    --accent-light: #f7b062;
    --venue-fill: #e3e3e3;
    --photo-dark: #2b2b2b;
    --photo-mid: #8a8a8a;
    --photo-light: #d6d6d6;
  }
  * { margin: 0; padding: 0; box-sizing: border-box; }
  html, body { width: 849px; height: 1200px; overflow: hidden; background: var(--ink); }
  .poster {
    position: relative;
    width: 849px;
    height: 1200px;
    background: var(--ink);
    color: var(--paper);
    overflow: hidden;
  }
  .artist-photo {
    position: absolute;
    left: 0; top: 0;
    width: 849px; height: 500px;
    background:
      radial-gradient(ellipse at 62% 35%, var(--photo-light) 0%, var(--photo-mid) 35%, transparent 70%),
      linear-gradient(90deg, var(--photo-dark) 0%, #555 30%, var(--photo-mid) 60%, #444 100%);
  }
  .title-band {
    position: absolute;
    left: 0; top: 455px;
    width: 849px; height: 290px;
  }
  .band-shape { position: absolute; left: 0; top: 0; }
  .artist-name {
    position: absolute;
    left: 0; right: 0; top: 88px;
    text-align: center;
    font-family: "Anton", "Oswald", sans-serif;
    font-size: 128px;
    line-height: 1;
    letter-spacing: 3px;
    color: var(--ink);
  }
  .star-row {
    position: absolute;
    left: 168px; top: 232px;
    width: 514px; height: 22px;
  }
  .credentials {
    position: absolute;
    left: 0; right: 0; top: 808px;
    text-align: center;
    font-family: "Oswald", sans-serif;
    white-space: nowrap;
  }
  .credentials-intro {
    font-weight: 700;
    font-size: 20px;
    line-height: 1.2;
    letter-spacing: 0.3px;
  }
  .credentials-highlights {
    margin-top: 2px;
    font-weight: 700;
    font-size: 34px;
    line-height: 1.15;
    letter-spacing: 0.2px;
  }
  .testimonial {
    position: absolute;
    left: 200px; right: 100px; top: 893px;
    text-align: center;
    font-family: "Lora", serif;
    font-style: italic;
    font-size: 30px;
    line-height: 1.25;
    white-space: nowrap;
  }
  .testimonial-source {
    position: absolute;
    right: 178px; top: 982px;
    font-family: "Oswald", sans-serif;
    font-weight: 700;
    font-size: 14px;
    letter-spacing: 0.3px;
  }
  .venue-box {
    position: absolute;
    left: 65px; top: 1010px;
    width: 719px; height: 130px;
    background: var(--paper);
    padding: 6px;
  }
  .tour-info {
    font-family: "Oswald", sans-serif;
    font-weight: 700;
    font-size: 20px;
    line-height: 1.2;
    text-align: center;
    color: var(--ink);
    padding: 2px 14px 6px;
  }
  .venue-details {
    margin-top: 4px;
    height: 82px;
    background: var(--venue-fill);
  }
</style>
</head>
<body>
<main class="poster">
  <div class="artist-photo" role="img" aria-label="Black and white portrait of the singer holding an acoustic guitar against a wooden wall"></div>

  <header class="title-band">
    <svg class="band-shape" width="849" height="290" viewBox="0 0 849 290" aria-hidden="true">
      <polygon fill="var(--accent-light)" points="0,22 30,14 58,24 90,10 122,20 150,8 186,18 214,6 246,20 280,10 312,22 344,8 378,18 410,6 440,20 474,10 506,24 540,8 572,18 604,6 636,20 668,10 700,22 732,8 764,18 796,6 826,20 849,12 849,40 0,40"/>
      <polygon fill="var(--accent)" points="0,30 28,22 60,34 92,20 126,30 158,18 190,30 222,16 254,28 288,18 318,32 350,18 384,28 416,16 448,30 480,20 512,32 546,18 578,28 610,16 642,30 674,20 706,32 738,18 770,28 802,16 832,30 849,22 849,268 820,278 790,264 758,276 726,262 694,274 662,260 630,276 598,264 566,278 534,262 502,274 470,260 438,276 406,264 374,278 342,262 310,274 278,260 246,276 214,264 182,278 150,262 118,274 86,260 54,276 22,264 0,274"/>
    </svg>
    <h1 class="artist-name">MARA PENWICK</h1>
    <svg class="star-row" viewBox="0 0 514 22" aria-hidden="true">
      <defs>
        <polygon id="star" points="11,0 13.6,7.6 21.5,7.6 15.1,12.3 17.5,20 11,15.3 4.5,20 6.9,12.3 0.5,7.6 8.4,7.6" fill="var(--ink)"/>
      </defs>
      <use href="#star" x="0"/><use href="#star" x="35"/><use href="#star" x="70"/><use href="#star" x="105"/>
      <use href="#star" x="140"/><use href="#star" x="175"/><use href="#star" x="210"/><use href="#star" x="245"/>
      <use href="#star" x="280"/><use href="#star" x="315"/><use href="#star" x="350"/><use href="#star" x="385"/>
      <use href="#star" x="420"/><use href="#star" x="455"/><use href="#star" x="490"/>
    </svg>
  </header>

  <section class="credentials">
    <p class="credentials-intro">NEW ZEALAND'S MOST PROLIFIC AND ACCOMPLISHED CHRISTIAN SINGER/SONGWRITER:</p>
    <p class="credentials-highlights">12 ALBUMS, 3 GOLD ALBUMS, 2 NZ MUSIC AWARDS</p>
  </section>

  <blockquote class="testimonial">"There is a depth in your songs that is<br>very rare in Christian music today."</blockquote>
  <p class="testimonial-source">VIDORRA COMMENT AUG 10, 2011</p>

  <section class="venue-box">
    <p class="tour-info">TOUR SCHEDULE &amp; INFO:&nbsp; WWW.MARAPENWICK.COM</p>
    <div class="venue-details"></div>
  </section>
</main>
</body>
</html>
```